Vosk and Telby Website

Vosk & Telby Website

The purpose of the Vosk & Telby website has 2 purposes; number 1 is to SALE the most “Rugged and Reliable products with the most versatile innovation possible. Number 2 to attract and assist territory sales manager across the United States with an easy flow website and customer sales support in the background.

Our Website Vision

This Website should be very modern and professional with a easy flow, we will use the following platform and plug-ins built with then website builder Divi Word press with Woo commerce with a sales professional CRM ( submit the plug-in of your choice for review before adding to programming) in the backend. We will provide information to the look we are looking for. All background images will be Black and White. We will provide professional images of our products that have been trimmed out and saved with a transparent background so that they can be added to a custom designed background or black and white image that will enhance the product. I want all the special tools provided in the Divi Family of tools used to give this website the WOW FACTOR. As of Now or site will be hosted on Plume Vault

Header design should have a Center VT Logo provided with a Hamburger Menu on the left and on the right a Search Glass Icon a Person Icon for login and register and Sales Cart Icon this could in the only Page that is Full Page Black and White image that can be blurred or ghosted back as we want the main page to be a line of 6 to 8 different Carts and Dollies to represent our products in color. Designer can take the images of our product and color correct Photoshop or whatever is needed to make it look its best. That is the landing or main image. The home page will be a slider of up to five images with 4 major messages to our customer or reasons to do business with Vosk & Telby. I will download 2 image to give you a idea of direction.

Slider Messages: Price Match Guarantee
Industry Best Warranty 5 Years on Frame 3 Years on Casters
Customize to fit your Surface and Application
Designed, Engineered and Manufactured Proudly in the U.S.A.

Categories/ Products Page
Carts
Dollies
Casters
Used Equipment

Categories Page

Products Page
Ratings with stars and comments
WooCommerce Composite products

Customization Page

Career Page

Contact page

Policy Page

Terms and Conditions Page

LOOK AT ZELMIRAB7BAY.COM WEBSITE MUST BE BETTER

Target Market(s)

We are a manufacturer of the worlds most rugged and reliable Industrial carts, dollies, hand trucks and casters. we will be selling to all types of industry's from distributors warehouse hospitals

Industry/Entity Type

Light Industrial

Coding

Coded - Design and coding required

Number of Pages Required

5+ page

Colors
ec1f27

Requirements
Must have
• Monochrome with Products colored and buttons and logo color codes in logo are Red # AF002A and Gray #5B5C5E
• Divi we own a lifetime license
• WordPress
• Woocommerce
• woocommerce composite products
• WP forms
• CRM
• Welder image is meant to be used Customization Page
Nice to have
• CRM for our 100 plus reps

```html
<!DOCTYPE html>
<html lang="en">
<head>
<meta charset="utf-8">
<title>Vosk &amp; Telby — Rugged and Reliable Versatile Innovation</title>
<link href="https://fonts.googleapis.com/css2?family=Anton&family=Raleway:wght@400;500;600;700&family=Quicksand:wght@400;500;600&family=Roboto:wght@500;700&display=swap" rel="stylesheet">
<style>
:root{
  --red:#c8102e;
  --red-bright:#dc1f48;
  --red-deep:#8e001f;
  --gray:#5b5c5e;
  --ink:#333436;
  --muted:#7a7b7d;
  --line:#cfcfcf;
  --white:#ffffff;
  --star:#f4b400;
}
*{margin:0;padding:0;box-sizing:border-box}
html,body{width:1200px;height:4083px;overflow:hidden;background:var(--white)}
body{position:relative;font-family:"Quicksand",sans-serif;color:var(--ink)}
.abs{position:absolute}
a{color:inherit;text-decoration:none}
ul{list-style:none}

/* header */
.brand{display:flex;align-items:center;gap:10px;font-family:"Raleway",sans-serif;font-weight:700;font-size:26px;color:var(--gray);letter-spacing:.5px}
.brand-mark{width:30px;height:30px;background:var(--red);border-radius:4px}
.site-header .brand{left:78px;top:28px}
.main-nav{left:415px;top:35px;display:flex;font-family:"Raleway",sans-serif;font-size:14px;font-weight:500;color:var(--gray);letter-spacing:.4px}
.main-nav a{margin-right:20px}
.header-tools{left:1025px;top:28px;display:flex;gap:5px}
.tool{width:31px;height:31px;border-radius:50%;background:var(--red);display:flex;align-items:center;justify-content:center}

/* hero */
.hero-title{left:76px;top:250px;font-family:"Anton",sans-serif;font-size:76px;line-height:82px;letter-spacing:1px;color:var(--ink)}
.hero-title span{display:block;color:var(--red)}
.hero-sub{left:79px;top:424px;font-family:"Raleway",sans-serif;font-size:19px;font-weight:500;color:var(--ink)}
.btn{display:inline-flex;align-items:center;justify-content:center;background:var(--red);color:var(--white);font-family:"Raleway",sans-serif;font-weight:700;border-radius:30px}
.hero-btn{left:78px;top:468px;width:249px;height:53px;font-size:18px}
.hero-product{left:540px;top:158px;width:570px;height:603px;border-radius:40px;background:radial-gradient(ellipse at 55% 45%,#d62a35 0%,#b8141f 40%,rgba(235,235,235,.6) 72%,rgba(255,255,255,0) 80%)}
.slider-dots{left:1149px;top:292px}
.slider-dots li{width:16px;height:16px;border:2px solid var(--red);border-radius:50%;margin-bottom:26px;position:relative}
.slider-dots li::after{content:"";position:absolute;left:3px;top:3px;width:6px;height:6px;border-radius:50%;background:var(--red)}
.slider-dots li.active::before{content:"";position:absolute;left:18px;top:6px;width:28px;height:1px;background:var(--ink)}

/* bands */
.band{left:0;width:1200px}
.about{top:780px;left:0;width:1200px;text-align:center;color:var(--white)}
.eyebrow{font-family:"Raleway",sans-serif;font-weight:600;font-size:20px;margin-top:22px}
.about h2{font-family:"Raleway",sans-serif;font-weight:600;font-size:40px;margin-top:6px}
.about p{width:680px;margin:22px auto 0;font-size:14.5px;line-height:27px}
.features{display:flex;justify-content:center;gap:15px;margin-top:44px}
.feature{width:157px;height:155px;background:rgba(255,255,255,.1);padding-top:22px}
.feature svg{display:block;margin:0 auto}
.feature h3{font-family:"Raleway",sans-serif;font-weight:600;font-size:19px;margin-top:18px}
.feature small{font-size:14.5px;display:block;margin-top:2px}
.ghost-word{left:130px;top:1130px;font-family:"Raleway",sans-serif;font-weight:700;font-size:170px;color:rgba(255,255,255,.06);transform:rotate(-8deg);white-space:nowrap}

/* categories */
.section-title{width:1200px;left:0;text-align:center;font-family:"Raleway",sans-serif;font-weight:600;font-size:41px;color:var(--ink)}
.section-title em{font-style:normal;color:var(--red)}
.section-sub{width:1200px;left:0;text-align:center;font-family:"Raleway",sans-serif;font-size:16px;color:var(--gray)}
.product-card{width:240px}
.product-photo{width:207px;height:207px;border-radius:50%;background:radial-gradient(circle at 50% 35%,#f2f2f2,#cfcfcf 80%)}
.product-card h3{font-family:"Raleway",sans-serif;font-weight:600;font-size:20px;color:var(--ink);margin-top:0}
.price{color:var(--red);font-size:17px;margin-top:4px}
.product-card p{font-size:13px;line-height:24px;color:var(--muted);margin-top:5px;width:215px}
.card-btn{width:135px;height:45px;font-size:15px;margin-top:14px}
.cart-icon{position:absolute;top:4px}
.rail{left:76px;top:2037px;width:1046px;height:1px;background:var(--line)}
.arrow-btn{width:41px;height:41px;border-radius:50%;border:1.5px solid var(--ink);background:var(--white);display:flex;align-items:center;justify-content:center}

/* innovation */
.welder{left:220px;top:2121px;width:760px;height:458px;background:radial-gradient(ellipse at 50% 55%,#b9b9b9 0%,#4a4a4a 45%,#141414 100%)}
.innovation{left:0;top:2612px;width:1200px;text-align:center;color:var(--white)}
.innovation h2{font-family:"Raleway",sans-serif;font-weight:600;font-size:43px}
.innovation p{width:660px;margin:18px auto 0;font-size:14.5px;line-height:27px}
.innovation .btn{width:187px;height:57px;font-size:18px;margin-top:28px;background:var(--red-bright)}

/* testimonials */
.quote{width:300px}
.quote p{font-style:italic;font-size:14.5px;line-height:29px;color:var(--muted);font-family:"Raleway",sans-serif}
.author{display:flex;align-items:center;margin-top:28px;gap:15px}
.avatar{width:71px;height:71px;border-radius:50%;background:radial-gradient(circle,#bfc4cc,#7d8694)}
.stars{color:var(--star);font-size:16px;letter-spacing:2px}
.author strong{display:block;color:var(--red);font-family:"Raleway",sans-serif;font-weight:700;font-size:16px;margin-top:2px}
.chev{top:3280px}

/* help */
.help{left:0;top:3508px;width:1200px;text-align:center;font-family:"Roboto",sans-serif;font-weight:500;font-size:31px;line-height:40px;color:var(--ink)}
.phone-btn{left:455px;top:3609px;width:290px;height:61px;border-radius:32px;background:var(--red);color:var(--white);display:flex;align-items:center;gap:18px;padding-left:10px;font-family:"Roboto",sans-serif;font-size:31px}
.phone-dot{width:46px;height:46px;border-radius:50%;background:var(--white);display:flex;align-items:center;justify-content:center}

/* footer */
.footer-col h4{font-family:"Raleway",sans-serif;font-weight:600;font-size:16px;color:var(--white);margin-bottom:14px}
.footer-col li{font-size:13.5px;color:var(--white);line-height:29px;position:relative;padding-left:22px}
.footer-col li::before{content:"";position:absolute;left:0;top:12px;width:5px;height:5px;border-radius:50%;background:var(--white)}
.site-footer .brand{left:78px;top:3882px;color:var(--white);font-size:24px}
.site-footer .brand-mark{background:var(--white)}
.footer-info{left:78px;top:3936px;width:225px;text-align:center;color:var(--white);font-size:15px}
.footer-info small{display:block;font-size:13px;line-height:23px;margin-top:10px}
</style>
</head>
<body>

<!-- background bands -->
<svg class="abs band" style="top:0" width="1200" height="4083" viewBox="0 0 1200 4083" aria-hidden="true">
  <defs>
    <linearGradient id="bandA" x1="0" y1="0" x2="1" y2="0">
      <stop offset="0" stop-color="#92001f"/>
      <stop offset="1" stop-color="#dc1f48"/>
    </linearGradient>
    <linearGradient id="bandB" x1="0" y1="0" x2="1" y2="0">
      <stop offset="0" stop-color="#dc1f48"/>
      <stop offset="1" stop-color="#8e001f"/>
    </linearGradient>
  </defs>
  <polygon points="0,800 1200,610 1200,1236 0,1427" fill="url(#bandA)"/>
  <polygon points="0,2362 1200,2544 1200,3099 0,2913" fill="url(#bandB)"/>
  <polygon points="0,3844 1200,3654 1200,4083 0,4083" fill="url(#bandA)"/>
</svg>

<header class="site-header">
  <a class="brand abs" href="#"><span class="brand-mark"></span>VOSK&amp;TELBY</a>
  <nav class="main-nav abs">
    <a href="#">CATEGORIES</a><a href="#">PRODUCTS</a><a href="#">CUSTOMIZATION</a><a href="#">CAREER</a><a href="#">CONTACT</a><a href="#">MORE...</a>
  </nav>
  <div class="header-tools abs">
    <span class="tool"><svg width="14" height="14" viewBox="0 0 14 14"><circle cx="6" cy="6" r="4" fill="none" stroke="#fff" stroke-width="2"/><line x1="9" y1="9" x2="13" y2="13" stroke="#fff" stroke-width="2"/></svg></span>
    <span class="tool"><svg width="14" height="14" viewBox="0 0 14 14"><circle cx="7" cy="4.5" r="3" fill="#fff"/><path d="M1.5 13.5a5.5 5 0 0 1 11 0z" fill="#fff"/></svg></span>
    <span class="tool"><svg width="15" height="14" viewBox="0 0 15 14"><path d="M1 1h2.5l2 8h7l1.5-6H4.5" fill="none" stroke="#fff" stroke-width="1.6"/><circle cx="6" cy="12" r="1.3" fill="#fff"/><circle cx="12" cy="12" r="1.3" fill="#fff"/></svg></span>
  </div>
</header>

<section class="hero">
  <div class="hero-product abs" role="img" aria-label="Red industrial two-tier utility cart with casters"></div>
  <h1 class="hero-title abs">PRICE MATCH<span>GUARANTEE</span></h1>
  <p class="hero-sub abs">Customize To Fit Your Surface And Application</p>
  <a class="btn hero-btn abs" href="#">SHOP BY CATEGORIES</a>
  <ul class="slider-dots abs"><li class="active"></li><li></li><li></li><li></li></ul>
</section>

<div class="ghost-word abs" aria-hidden="true">Vosk &amp; Telby</div>
<section class="about abs">
  <div class="eyebrow">About Us</div>
  <h2>Vosk &amp; Telby</h2>
  <p>Lorem Ipsum is simply dummy text of the printing and typesetting industry. Lorem Ipsum has been the industry's standard dummy text ever since the 1500s, when an unknown printer took a galley of type and scrambled it to make a type specimen book.</p>
  <div class="features">
    <div class="feature">
      <svg width="36" height="52" viewBox="0 0 36 52" fill="none" stroke="#fff" stroke-width="2"><circle cx="18" cy="17" r="15"/><circle cx="18" cy="17" r="9"/><path d="M10 29l-4 20 6-4 4 6 3-13M26 29l4 20-6-4-4 6"/></svg>
      <h3>5 Years</h3><small>Best Warranty</small>
    </div>
    <div class="feature">
      <svg width="50" height="50" viewBox="0 0 50 50" fill="none" stroke="#fff" stroke-width="2.4"><path d="M2 14V2h12M36 2h12v12M48 36v12H36M14 48H2V36"/></svg>
      <h3>3 Years</h3><small>Frame on Casters</small>
    </div>
    <div class="feature">
      <svg width="30" height="52" viewBox="0 0 30 52" fill="none" stroke="#fff" stroke-width="2"><path d="M10 12L15 4l5 8h7v38H3V12z"/><circle cx="15" cy="17" r="2"/><text x="15" y="40" fill="#fff" stroke="none" font-size="15" text-anchor="middle" font-family="Quicksand,sans-serif">$</text></svg>
      <h3>Price</h3><small>Match Guarantee</small>
    </div>
  </div>
</section>

<section class="categories">
  <h2 class="section-title abs" style="top:1410px">CATEG<em>ORIES</em></h2>
  <p class="section-sub abs" style="top:1467px">Rugged and Reliable Versative Innovation</p>

  <article class="product-card abs" style="left:89px;top:1537px">
    <div class="product-photo" style="margin-left:13px" role="img" aria-label="Steel hand truck in a warehouse"></div>
    <h3 style="margin-top:66px">Carts</h3>
    <div class="price">$360.0000</div>
    <p>Lorem Ipsum is simply dummy text of the printing and</p>
    <a class="btn card-btn" href="#">VIEW DETAIL</a>
    <svg class="cart-icon" style="left:203px;top:276px" width="20" height="18" viewBox="0 0 20 18"><path d="M1 1h3l2.5 10h9.5l2-8H5" fill="none" stroke="#c8102e" stroke-width="2"/><circle cx="8" cy="15.5" r="1.6" fill="#c8102e"/><circle cx="15" cy="15.5" r="1.6" fill="#c8102e"/></svg>
  </article>

  <article class="product-card abs" style="left:353px;top:1537px">
    <div class="product-photo" style="margin-left:10px" role="img" aria-label="Blue platform dolly in a warehouse"></div>
    <h3 style="margin-top:66px">Dollies</h3>
    <div class="price">$360.0000</div>
    <p>Lorem Ipsum is simply dummy text of the printing and</p>
    <a class="btn card-btn" href="#">VIEW DETAIL</a>
    <svg class="cart-icon" style="left:208px;top:276px" width="20" height="18" viewBox="0 0 20 18"><path d="M1 1h3l2.5 10h9.5l2-8H5" fill="none" stroke="#c8102e" stroke-width="2"/><circle cx="8" cy="15.5" r="1.6" fill="#c8102e"/><circle cx="15" cy="15.5" r="1.6" fill="#c8102e"/></svg>
  </article>

  <article class="product-card abs" style="left:623px;top:1537px">
    <div class="product-photo" style="margin-left:10px" role="img" aria-label="Blue convertible hand truck in a warehouse"></div>
    <h3 style="margin-top:66px">Casters</h3>
    <div class="price">$360.0000</div>
    <p>Lorem Ipsum is simply dummy text of the printing and</p>
    <a class="btn card-btn" href="#">VIEW DETAIL</a>
    <svg class="cart-icon" style="left:201px;top:276px" width="20" height="18" viewBox="0 0 20 18"><path d="M1 1h3l2.5 10h9.5l2-8H5" fill="none" stroke="#c8102e" stroke-width="2"/><circle cx="8" cy="15.5" r="1.6" fill="#c8102e"/><circle cx="15" cy="15.5" r="1.6" fill="#c8102e"/></svg>
  </article>

  <article class="product-card abs" style="left:891px;top:1537px">
    <div class="product-photo" style="margin-left:10px" role="img" aria-label="Red two-tier utility cart in a warehouse"></div>
    <h3 style="margin-top:66px">Used Equipment</h3>
    <div class="price">$360.0000</div>
    <p>Lorem Ipsum is simply dummy text of the printing and</p>
    <a class="btn card-btn" href="#">VIEW DETAIL</a>
    <svg class="cart-icon" style="left:201px;top:276px" width="20" height="18" viewBox="0 0 20 18"><path d="M1 1h3l2.5 10h9.5l2-8H5" fill="none" stroke="#c8102e" stroke-width="2"/><circle cx="8" cy="15.5" r="1.6" fill="#c8102e"/><circle cx="15" cy="15.5" r="1.6" fill="#c8102e"/></svg>
  </article>

  <div class="rail abs"></div>
  <span class="arrow-btn abs" style="left:555px;top:2017px"><svg width="10" height="14" viewBox="0 0 10 14"><path d="M8 1L2 7l6 6" fill="none" stroke="#333" stroke-width="1.6"/></svg></span>
  <span class="arrow-btn abs" style="left:603px;top:2017px"><svg width="10" height="14" viewBox="0 0 10 14"><path d="M2 1l6 6-6 6" fill="none" stroke="#333" stroke-width="1.6"/></svg></span>
</section>

<section>
  <div class="welder abs" role="img" aria-label="Black and white photo of a welder at work with sparks flying"></div>
  <div class="innovation abs">
    <h2>Versative Innovation</h2>
    <p>Lorem Ipsum is simply dummy text of the printing and typesetting industry. Lorem Ipsum has been the industry's standard dummy text ever since the 1500s, when an unknown printer took a galley of type and scrambled it to make a type specimen book Lorem Ipsum is simply dummy text of the printing and typesetting industry. Lorem Ipsum has been the industry's standard dummy text</p>
    <a class="btn" href="#">LEARN MORE</a>
  </div>
</section>

<section class="testimonials">
  <h2 class="section-title abs" style="top:3095px">WHAT OUR <em>CLIENT SAY</em></h2>
  <p class="section-sub abs" style="top:3151px">Testimonials</p>

  <svg class="abs chev" style="left:30px" width="18" height="34" viewBox="0 0 18 34"><path d="M16 1L2 17l14 16" fill="none" stroke="#999" stroke-width="1.5"/></svg>
  <svg class="abs chev" style="left:1155px" width="18" height="34" viewBox="0 0 18 34"><path d="M2 1l14 16L2 33" fill="none" stroke="#999" stroke-width="1.5"/></svg>

  <blockquote class="quote abs" style="left:97px;top:3202px">
    <p>" Lorem Ipsum is simply dummy text of the printing and typesetting industry. Lorem Ipsum has been the industry's standard dummy text "</p>
    <div class="author"><span class="avatar" role="img" aria-label="Client portrait"></span><div><span class="stars">★★★★★</span><strong>Client Name</strong></div></div>
  </blockquote>
  <blockquote class="quote abs" style="left:456px;top:3202px">
    <p>" Lorem Ipsum is simply dummy text of the printing and typesetting industry. Lorem Ipsum has been the industry's standard dummy text "</p>
    <div class="author"><span class="avatar" role="img" aria-label="Client portrait"></span><div><span class="stars">★★★★★</span><strong>Client Name</strong></div></div>
  </blockquote>
  <blockquote class="quote abs" style="left:821px;top:3202px">
    <p>" Lorem Ipsum is simply dummy text of the printing and typesetting industry. Lorem Ipsum has been the industry's standard dummy text "</p>
    <div class="author"><span class="avatar" role="img" aria-label="Client portrait"></span><div><span class="stars">★★★★★</span><strong>Client Name</strong></div></div>
  </blockquote>
</section>

<section>
  <h2 class="help abs">Need Help? Call our Solution<br>Specialists Today!</h2>
  <a class="phone-btn abs" href="#"><span class="phone-dot"><svg width="22" height="22" viewBox="0 0 24 24"><path d="M6.6 10.8a15 15 0 0 0 6.6 6.6l2.2-2.2a1 1 0 0 1 1-.25 11.4 11.4 0 0 0 3.6.6 1 1 0 0 1 1 1V20a1 1 0 0 1-1 1A17 17 0 0 1 3 4a1 1 0 0 1 1-1h3.5a1 1 0 0 1 1 1c0 1.25.2 2.45.6 3.6a1 1 0 0 1-.25 1z" fill="#c8102e"/></svg></span>123.456.7890</a>
</section>

<footer class="site-footer">
  <a class="brand abs" href="#"><span class="brand-mark"></span>VOSK&amp;TELBY</a>
  <div class="footer-info abs">info@vosktelby.com<small>©Vosk &amp; Telby - 2019 All<br>Rights Reserved</small></div>

  <div class="footer-col abs" style="left:352px;top:3828px">
    <h4>SITEMAP</h4>
    <ul><li>Categories</li><li>Products</li><li>Customization</li><li>Career</li><li>Testimonials</li><li>Contact</li></ul>
  </div>
  <div class="footer-col abs" style="left:536px;top:3828px">
    <h4>CATEGORIES</h4>
    <ul><li>Carts</li><li>Dollies</li><li>Casters</li><li>Used Equipment</li></ul>
  </div>
  <div class="footer-col abs" style="left:736px;top:3828px">
    <h4>QUICK LINKS</h4>
    <ul><li>Faq's</li><li>Return Policy</li><li>Best Price Guarantee</li><li>Shipping Informatio</li><li>Policy Page</li><li>Terms and Conditions</li></ul>
  </div>
  <div class="footer-col abs" style="left:954px;top:3828px">
    <h4>FOLLOW US</h4>
    <ul><li>Facenote</li><li>Chirper</li><li>Linkfold</li><li>Snapgram</li><li>Viewtube</li></ul>
  </div>
</footer>

</body>
</html>
```